Start-up Cleaning Business Needs Professional Business Cards

Marisol's Butler Tidying, LLC, is a start-up business based in the Northern Virginia suburbs of Washington, DC. MBT provides cleaning and housekeeping services for homes and offices. We have three core values:

1. We are personal. We value knowing and being known by our customers and each other. If you want nameless, faceless service, you should choose another provider. We put "personal" at the front of the list, because it is most important to us; the design we choose will convey this value.

2. Like a hotel concierge, we are professional in attitude, posture, communication and processes.

3. Like a hotel concierge, we solve problems with a can-do attitude and never make excuses.

Our uniforms are khaki pants with pink polo shirts.

Our logo is attached. There are other symbols, not represented in our logo, that may convey our values well, such as a top hat and bow tie, magnifying glass, desk bell, etc.

Please include fields for an individual's name and title, office phone number, mobile phone number, email address and website address (www.marisolsbutlertidying-example.com).

Standard U.S. size: 2" x 3.5"
Updates

I should have mentioned that the purpose of all our advertising - business cards included - is to motivate potential customers to call or email to arrange a free in-home estimate.

```html
<!DOCTYPE html>
<html lang="en">
<head>
<meta charset="utf-8">
<title>Marisol's Butler Tidying — Business Cards</title>
<link rel="stylesheet" href="https://fonts.googleapis.com/css2?family=Open+Sans:wght@400;600&display=swap">
<style>
  :root {
    --canvas: #d1d1d3;
    --card: #ffffff;
    --trim: #ec5aa6;
    --frame: #4a4a4a;
    --band: #3e3c3d;
    --ink: #2e2e2e;
    --band-text: #ffffff;
    --art-pink: #e0559b;
    --art-brown: #a9806b;
  }
  * { box-sizing: border-box; margin: 0; padding: 0; }
  html, body { width: 883px; height: 1200px; overflow: hidden; }
  body {
    background: var(--canvas);
    font-family: "Open Sans", Arial, sans-serif;
    color: var(--ink);
    position: relative;
  }
  .card {
    position: absolute;
    left: 91px;
    width: 700px;
    height: 392px;
    background: var(--card);
    box-shadow: 0 2px 6px rgba(0,0,0,.12);
  }
  .card--front { top: 188px; }
  .card--back { top: 620px; }
  .card__trim {
    position: absolute; inset: 6px;
    border: 1.5px solid var(--trim);
  }
  .card__frame {
    position: absolute; left: 36px; right: 36px; top: 32px; bottom: 29px;
    border: 1.5px solid var(--frame);
  }
  .band {
    position: absolute; left: 36px; right: 36px;
    background: var(--band);
  }
  .card--front .band { top: 274px; height: 72px; }
  .card--back .band { top: 230px; bottom: 29px; }
  .illustration {
    position: absolute;
    background: linear-gradient(160deg, var(--art-pink) 0%, #f3c3da 45%, #e9ddd6 75%, var(--art-brown) 100%);
    opacity: .55;
    border-radius: 6px;
  }
  .card--front .illustration { left: 265px; top: 47px; width: 171px; height: 227px; }
  .card--back .illustration { left: 445px; top: 41px; width: 117px; height: 189px; }
  .wordmark {
    position: absolute;
    color: var(--band-text);
    font-weight: 400;
    text-align: center;
    line-height: 1.05;
  }
  .wordmark__name { display: block; font-size: 38px; }
  .wordmark__tag { display: block; font-size: 14px; letter-spacing: 1.5px; margin-top: 2px; }
  .card--front .wordmark { left: 200px; width: 300px; top: 282px; }
  .card--back .wordmark { left: 400px; width: 210px; top: 240px; }
  .card--back .wordmark__name { font-size: 34px; }
  .person { position: absolute; left: 65px; top: 108px; }
  .person__name { font-size: 25px; font-weight: 400; letter-spacing: .3px; }
  .person__title { font-size: 17px; margin-top: 6px; margin-left: 21px; }
  .contact {
    position: absolute; left: 56px; top: 241px;
    list-style: none; color: var(--band-text);
    font-size: 19px; line-height: 20.8px;
  }
  .contact li { display: flex; align-items: center; height: 20.8px; }
  .contact__icon {
    width: 18px; margin-right: 12px;
    display: inline-flex; justify-content: center;
    font-size: 12px; font-weight: 600;
  }
  .contact__icon svg { width: 13px; height: 13px; }
</style>
</head>
<body>

<section class="card card--front" aria-label="Business card front">
  <div class="card__trim"></div>
  <div class="card__frame"></div>
  <div class="band"></div>
  <div class="illustration" role="img" aria-label="Hand-drawn illustration of a housekeeper in pink sweeping with a mop"></div>
  <div class="wordmark">
    <span class="wordmark__name">Marisol's</span>
    <span class="wordmark__tag">Butler Tidying</span>
  </div>
</section>

<section class="card card--back" aria-label="Business card back">
  <div class="card__trim"></div>
  <div class="card__frame"></div>
  <div class="band"></div>
  <div class="illustration" role="img" aria-label="Hand-drawn illustration of a housekeeper in pink sweeping with a mop"></div>
  <div class="person">
    <p class="person__name">YOUR NAME</p>
    <p class="person__title">TITLE HERE</p>
  </div>
  <ul class="contact">
    <li><span class="contact__icon"><svg viewBox="0 0 16 16" fill="#fff"><path d="M2 5c0-2 1-3 6-3s6 1 6 3l-3 1-1-2H6L5 6 2 5zM4 7h8l2 7H2l2-7zm4 2a2 2 0 100 4 2 2 0 000-4z"/></svg></span>0123 456 789</li>
    <li><span class="contact__icon"><svg viewBox="0 0 16 16" fill="none" stroke="#fff" stroke-width="1.6"><rect x="4" y="1" width="8" height="14" rx="1"/></svg></span>0123 456 789</li>
    <li><span class="contact__icon">Fx</span>0123 456 789</li>
    <li><span class="contact__icon"><svg viewBox="0 0 16 16" fill="#fff"><path d="M1 3h14v10H1z"/><path d="M1 3l7 6 7-6" fill="none" stroke="#3e3c3d" stroke-width="1.4"/></svg></span>youremail@mail.com</li>
    <li><span class="contact__icon"><svg viewBox="0 0 16 16" fill="none" stroke="#fff" stroke-width="1.3"><circle cx="8" cy="8" r="6.5"/><ellipse cx="8" cy="8" rx="3" ry="6.5"/><path d="M1.5 8h13"/></svg></span>www.yourwebdite.com</li>
  </ul>
</section>

</body>
</html>
```